Looking for a modern website banner design

Corvella Fieldmark Consultants looking for the development of the main banner of the website. The project description and photos are included in the upload files.

```html
<!DOCTYPE html>
<html lang="en">
<head>
<meta charset="utf-8">
<title>Corvella Fieldmark Consultants — Athlete Testimonial Banner</title>
<link rel="stylesheet" href="https://fonts.googleapis.com/css2?family=Poppins:ital,wght@0,400;0,600;1,300;1,500&display=swap">
<style>
  :root {
    --panel-dark: #2e2e30;
    --panel-dark-deep: #262628;
    --accent-blue: #1570c4;
    --name-blue: #2a95e8;
    --text-light: #ffffff;
    --photo-deep: #2a1c1f;
    --photo-red: #8a2430;
    --photo-board: #d9d6cf;
  }
  * { margin: 0; padding: 0; box-sizing: border-box; }
  html, body { width: 1200px; height: 562px; overflow: hidden; background: var(--panel-dark); }
  .banner {
    position: relative;
    width: 1200px;
    height: 562px;
    overflow: hidden;
    font-family: "Poppins", sans-serif;
    color: var(--text-light);
  }
  .banner__photo {
    position: absolute;
    inset: 0;
    background:
      linear-gradient(180deg, transparent 0%, transparent 58%, var(--photo-board) 60%, var(--photo-board) 88%, #d8cf6a 92%),
      radial-gradient(ellipse at 72% 45%, var(--photo-red) 0%, transparent 45%),
      linear-gradient(90deg, #3a2a2c 0%, var(--photo-deep) 50%, #3d3438 100%);
  }
  .banner__shapes { position: absolute; inset: 0; }
  .testimonial {
    position: absolute;
    left: 46px;
    top: 74px;
    width: 370px;
    text-align: center;
  }
  .testimonial__quote {
    font-size: 19px;
    line-height: 26.3px;
    font-style: italic;
    font-weight: 300;
  }
  .testimonial__quote strong { font-weight: 500; }
  .athlete {
    position: absolute;
    left: 46px;
    top: 283px;
    width: 370px;
    text-align: center;
  }
  .athlete__portrait {
    display: block;
    width: 128px;
    height: 128px;
    margin: 0 auto;
    border-radius: 50%;
    background: radial-gradient(circle at 50% 40%, #7a6552 0%, #3a2f2a 70%, #1f2436 100%);
  }
  .athlete__name {
    margin-top: 16px;
    font-size: 19px;
    font-weight: 600;
    color: var(--name-blue);
    line-height: 1.2;
  }
  .athlete__team {
    margin-top: 8px;
    font-size: 15px;
    font-weight: 400;
    line-height: 20px;
  }
</style>
</head>
<body>
  <section class="banner">
    <div class="banner__photo" role="img" aria-label="Photo of a hockey player in a red and black jersey celebrating on the ice, arms raised, with cheering fans behind the glass"></div>

    <svg class="banner__shapes" width="1200" height="562" viewBox="0 0 1200 562" aria-hidden="true">
      <defs>
        <linearGradient id="panelShade" x1="0" y1="0" x2="1" y2="1">
          <stop offset="0" stop-color="var(--panel-dark-deep)"/>
          <stop offset="0.5" stop-color="var(--panel-dark)"/>
          <stop offset="1" stop-color="var(--panel-dark-deep)"/>
        </linearGradient>
      </defs>
      <path d="M0,0 H418 C505,110 585,280 570,420 C563,480 535,530 505,562 H0 Z" fill="var(--accent-blue)"/>
      <path d="M0,0 H400 C490,125 545,290 538,420 C534,480 516,530 497,562 H0 Z" fill="url(#panelShade)"/>
    </svg>

    <blockquote class="testimonial">
      <p class="testimonial__quote">
        <strong>“Corvella has provided support that has allowed me to develop as a person and an athlete.</strong>
        The P.A.C.E.™ process allowed me to stay focused on attainable goals each season and progress from Junior to College and now Professional Hockey.”
      </p>
    </blockquote>

    <div class="athlete">
      <span class="athlete__portrait" role="img" aria-label="Portrait photo of the athlete in a hockey helmet"></span>
      <p class="athlete__name">Dorian Ashcombe</p>
      <p class="athlete__team">Lakemont Comets<br>Atlantic Ridge Hockey League</p>
    </div>
  </section>
</body>
</html>
```